Author book launch promotion design for social media

We are organising an authors book launch event and require an author promotion design that will be used on social media (Chatterly, netwise) promotion.

The design must have the author's photo, image of their book, the event logo, details of the event plus website address (quillfairhub.com.au).

Details of the event can be found at quillfairhub.com.au.

the design has to be attractive and inviting and colours in accordance with the brand colours.

You can choose 1 one of the book images attached
Author name: Dr Tobias Merrill
Event Details
LAUNCH YOUR BOOK IN STYLE

Pagecraft Reading Fair 2022
7 - 8 October 2022
Melbourne Larkfield Pavilion
14 Corrigan St, Southbank Melbourne

For registration and ticketing visit:
quillfairhub.com.au

I have attached also a sample promo. Please be creative.

```html
<!DOCTYPE html>
<html lang="en">
<head>
<meta charset="utf-8">
<title>Dr Tobias Merrill – Pagecraft Reading Fair 2022</title>
<link rel="stylesheet" href="https://fonts.googleapis.com/css2?family=Questrial&family=Poppins:wght@500;600&family=PT+Sans:wght@700&display=swap">
<style>
  :root {
    --brand-blue: #2f6393;
    --brand-red: #d2405a;
    --brand-gold: #c49a35;
    --jacket: #2c2f35;
    --text-grey: #6b6b6b;
    --paper: #f3f3f4;
    --paper-light: #ffffff;
  }
  * { margin: 0; padding: 0; box-sizing: border-box; }
  html, body { width: 1200px; height: 1070px; overflow: hidden; }
  body { background: var(--paper); }
  .promo {
    position: relative;
    width: 1200px;
    height: 1070px;
    overflow: hidden;
    background: radial-gradient(circle at 32% 60%, var(--paper-light) 0%, var(--paper) 62%);
    font-family: "Questrial", sans-serif;
  }
  .event-mark {
    position: absolute;
    left: 36px;
    top: 58px;
    display: flex;
    align-items: center;
    gap: 14px;
  }
  .event-mark__dot {
    width: 38px;
    height: 38px;
    border-radius: 50%;
    background: var(--brand-gold);
  }
  .event-mark__name {
    font-family: "Poppins", sans-serif;
    font-weight: 600;
    font-size: 48px;
    letter-spacing: 1px;
    color: var(--brand-gold);
    line-height: 1;
  }
  .invite {
    position: absolute;
    left: 35px;
    top: 248px;
    color: var(--brand-blue);
    font-size: 43px;
    line-height: 50px;
    white-space: nowrap;
  }
  .invite strong {
    font-family: "PT Sans", sans-serif;
    font-weight: 700;
    font-size: 42px;
  }
  .author-portrait {
    position: absolute;
    left: 680px;
    top: -200px;
    width: 782px;
    height: 782px;
    border-radius: 50%;
    background:
      radial-gradient(ellipse 42% 50% at 40% 88%, var(--jacket) 0%, var(--jacket) 55%, rgba(44,47,53,0) 100%),
      var(--brand-blue);
  }
  .book-image {
    position: absolute;
    left: 113px;
    top: 461px;
    width: 422px;
    height: 440px;
    border-radius: 4px;
    background: linear-gradient(180deg, #ececec 0%, #b8bcc3 35%, #3e4a5c 75%, #c9475e 100%);
  }
  .details {
    position: absolute;
    right: 36px;
    text-align: right;
    line-height: 1;
    white-space: nowrap;
  }
  .details--name {
    top: 606px;
    font-family: "PT Sans", sans-serif;
    font-weight: 700;
    font-size: 50px;
    color: var(--brand-red);
  }
  .details--role {
    top: 660px;
    font-family: "PT Sans", sans-serif;
    font-weight: 700;
    font-size: 40px;
    color: var(--brand-blue);
  }
  .details--event {
    top: 772px;
    font-family: "Poppins", sans-serif;
    font-weight: 500;
    font-size: 35px;
    color: var(--brand-red);
  }
  .details--date {
    top: 862px;
    font-family: "Poppins", sans-serif;
    font-weight: 600;
    font-size: 60px;
    color: var(--brand-blue);
  }
  .details--venue {
    top: 951px;
    font-family: "Poppins", sans-serif;
    font-weight: 500;
    font-size: 26px;
    color: var(--brand-blue);
  }
  .details--address {
    top: 1004px;
    font-family: "Poppins", sans-serif;
    font-weight: 500;
    font-size: 26px;
    color: var(--brand-blue);
  }
  .registration {
    position: absolute;
    left: 34px;
    top: 972px;
    line-height: 1;
  }
  .registration__label {
    font-size: 25px;
    color: var(--text-grey);
  }
  .registration__url {
    margin-top: 14px;
    font-family: "Poppins", sans-serif;
    font-weight: 500;
    font-size: 25px;
    color: var(--brand-red);
  }
</style>
</head>
<body>
  <main class="promo">
    <div class="event-mark">
      <span class="event-mark__dot"></span>
      <span class="event-mark__name">QUILLFAIR</span>
    </div>

    <p class="invite">You are invited to a unique event<br>to <strong>LAUNCH YOUR BOOK IN STYLE.</strong></p>

    <div class="author-portrait" role="img" aria-label="Portrait photo of author Dr Tobias Merrill, smiling, in glasses and a dark blazer, set in a blue circle"></div>

    <div class="book-image" role="img" aria-label="Product photo of Dr Tobias Merrill's book standing upright on a second copy lying flat with a red spine"></div>

    <p class="details details--name">Dr Tobias Merrill</p>
    <p class="details details--role">Author</p>
    <p class="details details--event">Pagecraft Reading Fair 2022</p>
    <p class="details details--date">7 - 8 October 2022</p>
    <p class="details details--venue">Melbourne Larkfield Pavilion</p>
    <p class="details details--address">14 Corrigan St, Southbank Melbourne</p>

    <div class="registration">
      <p class="registration__label">For registration and ticketing visit:</p>
      <p class="registration__url">quillfairhub.com.au</p>
    </div>
  </main>
</body>
</html>
```